Small consulting business needs logo and business card design

I need a logo, business card and letterhead design for a small consulting firm called Veltramo Consulting. My customers are generally small to medium sized businesses but I have done work for major corporates and government departments. The field of consulting is strategic/business planning and program management. I have blue as the predominate colour in my current business card but I am happy to change this for the right design
Industry/Entity Type
Business

```html
<!DOCTYPE html>
<html lang="en">
<head>
<meta charset="utf-8">
<title>Veltramo Consulting – Business Card</title>
<link rel="stylesheet" href="https://fonts.googleapis.com/css2?family=Open+Sans:wght@400;600&display=swap">
<style>
  :root {
    --page-bg: #e4e4e4;
    --card-bg: #f7f7f7;
    --brand-blue: #1a4c9c;
    --text-dark: #3c3c3c;
    --text-muted: #6a6a6a;
    --on-blue: #ffffff;
  }
  * { box-sizing: border-box; margin: 0; padding: 0; }
  html, body {
    width: 1200px;
    height: 1200px;
    overflow: hidden;
    background: var(--page-bg);
    font-family: "Open Sans", Arial, sans-serif;
  }
  .canvas {
    width: 1200px;
    height: 1200px;
    display: flex;
    align-items: center;
    justify-content: center;
  }
  .business-card {
    position: relative;
    width: 1050px;
    height: 600px;
    background: var(--card-bg);
    box-shadow: 0 6px 24px rgba(0, 0, 0, 0.12);
    overflow: hidden;
  }
  .brand {
    position: absolute;
    left: 470px;
    top: 105px;
    display: flex;
    align-items: center;
    gap: 18px;
  }
  .brand-mark {
    width: 58px;
    height: 58px;
    border-radius: 50%;
    background: var(--brand-blue);
  }
  .brand-name {
    font-size: 44px;
    font-weight: 600;
    color: var(--brand-blue);
    letter-spacing: 0.5px;
  }
  .address {
    position: absolute;
    left: 70px;
    top: 232px;
    font-size: 19px;
    line-height: 1.4;
    color: var(--text-muted);
  }
  .name-band {
    position: absolute;
    left: 450px;
    right: 0;
    top: 250px;
    height: 62px;
    background: var(--brand-blue);
    display: flex;
    align-items: center;
    padding-left: 50px;
  }
  .name-band span {
    color: var(--on-blue);
    font-size: 21px;
    letter-spacing: 1px;
  }
  .contact-list {
    position: absolute;
    left: 440px;
    top: 335px;
    list-style: none;
  }
  .contact-item {
    display: flex;
    align-items: center;
    gap: 12px;
    font-size: 24px;
    line-height: 1.6;
    color: var(--text-dark);
  }
  .contact-icon {
    width: 20px;
    height: 20px;
    border-radius: 4px;
    background: var(--brand-blue);
    display: flex;
    align-items: center;
    justify-content: center;
  }
  .contact-icon svg { width: 14px; height: 14px; }
</style>
</head>
<body>
<main class="canvas">
  <section class="business-card">
    <div class="brand">
      <span class="brand-mark"></span>
      <span class="brand-name">Veltramo Consulting</span>
    </div>

    <p class="address">Address : xxxxx xxxxxx<br>xxxxx xxx212, xxxxxxx</p>

    <div class="name-band"><span>XXXX XXXXX</span></div>

    <ul class="contact-list">
      <li class="contact-item">
        <span class="contact-icon">
          <svg viewBox="0 0 14 14"><path d="M3 1.5 L5 1.5 L6 4.5 L4.7 5.5 Q5.8 8 8.5 9.3 L9.5 8 L12.5 9 L12.5 11 Q12 12.5 10.5 12.5 Q2 12 1.5 3.5 Q1.5 2 3 1.5 Z" fill="#fff"/></svg>
        </span>
        Phone No. (TBA Later)
      </li>
      <li class="contact-item">
        <span class="contact-icon">
          <svg viewBox="0 0 14 14"><rect x="1.5" y="3" width="11" height="8" fill="none" stroke="#fff" stroke-width="1.4"/><path d="M1.5 3 L7 8 L12.5 3" fill="none" stroke="#fff" stroke-width="1.4"/></svg>
        </span>
        Email address (TBA Later)
      </li>
      <li class="contact-item">
        <span class="contact-icon">
          <svg viewBox="0 0 14 14"><circle cx="7" cy="7" r="5.3" fill="none" stroke="#fff" stroke-width="1.3"/><ellipse cx="7" cy="7" rx="2.3" ry="5.3" fill="none" stroke="#fff" stroke-width="1.1"/><path d="M1.7 7 H12.3" stroke="#fff" stroke-width="1.1"/></svg>
        </span>
        Web address (TBA Later)
      </li>
    </ul>
  </section>
</main>
</body>
</html>
```